Web Design Project - Management Consulting Firm Firm

We need a design to upgrade our website. The design should reflect the core values , branding of the firm & must be benchmarked with the best management consulting firms in the world.

It should have right choice of images , have evoke words / captions that will attract traffic & must be the best design for a contemporary management consulting firm

current website - www.tallbirchwood.biz
Updates

Hello Designers

we are keen to take our website to next level. It should be benchmarked with best management consulting firm's website on look and feel..

i have uploaded the corporate profile ,  mkt strategy..

email me for any clarifications..

Good Luck

Vikas

Project Deadline Extended
Reason: We want the best Design!! and we want to extend the deadline by 3 more days.. 10 Days to go..

Any takers??

Target Market(s)

CFO / CIO / CEO / Business owners & Decision makers

Industry/Entity Type

Management Consulting

Requirements
Must have
• Lively ; but not flashy or flamboyant.

It should reflect the brand values / TBW positioning that I will be sharing .

Benchmark and compare with the best consulting firm websites

Nice to have
• Images..but nothing flashy..

benchmark with leading consulting firms websites..
1.norvitane
2.Pravelle
3. Harwick Advisory Group
4. Tilden & Crowe
5. Fairloch
6. Voss Consulting
Should not have
• Too loud.

```html
<!DOCTYPE html>
<html lang="en">
<head>
<meta charset="utf-8">
<title>TBW – Management Consulting</title>
<link rel="stylesheet" href="https://fonts.googleapis.com/css2?family=Arimo:wght@400;700&family=Roboto+Condensed:wght@400;700&display=swap">
<style>
:root{
  --navy:#2b2a72;
  --red:#d0021b;
  --orange-red:#cf3a0e;
  --ink:#222;
  --grey-text:#8a8a8a;
  --rule:#dcdcdc;
  --logo-grey:#9a9a9a;
}
*{margin:0;padding:0;box-sizing:border-box}
html,body{width:1200px;height:1121px;overflow:hidden;background:#fff}
body{position:relative;font-family:"Arimo",Arial,sans-serif;color:var(--ink)}
.abs{position:absolute}

.brand{left:141px;top:20px}
.brand-name{font-family:"Arimo",Arial,sans-serif;font-weight:400;font-size:80px;line-height:80px;color:var(--navy)}

.utility-links{right:141px;top:23px;font-size:11.5px;color:#222}
.utility-links span{margin:0 5px}

.search{left:859px;top:88px;width:200px;height:26px;border:1px solid #ccc}
.search-button{position:absolute;right:-1px;top:-1px;width:31px;height:26px;background:var(--red)}

.main-nav{left:141px;top:139px;width:918px;height:37px;background:var(--navy);display:flex;font-size:13.5px;color:#fff;letter-spacing:.4px}
.main-nav a{color:#fff;text-decoration:none;line-height:37px;padding:0 21px}
.main-nav a.active{background:var(--orange-red);width:82px;text-align:center;padding:0}

.hero{left:141px;top:194px;width:918px;height:319px;border:1px solid #e2e2e2;overflow:hidden}
.hero-photo{position:absolute;left:270px;top:0;right:0;bottom:0;background:linear-gradient(90deg,#fff 0%,#f1f1f1 30%,#e4e4e6 65%,#d8d8da 100%)}
.hero-headline{position:absolute;left:25px;top:46px;font-family:"Arimo",Arial,sans-serif;font-weight:700;color:var(--orange-red);line-height:34px}
.hero-headline .sm{font-size:22px}
.hero-headline .lg{font-size:35px}
.hero-copy{position:absolute;left:25px;top:140px;width:256px;font-size:13.5px;line-height:16px;color:#555;text-align:justify}

.feature{top:548px;width:281px}
.feature h2{font-family:"Roboto Condensed",Arial,sans-serif;font-weight:400;font-size:17.5px;color:var(--red);letter-spacing:.1px}
.feature h3{font-weight:400;font-size:13.5px;line-height:16px;color:var(--ink);margin-top:14px;height:32px}
.feature p{font-size:10.5px;line-height:14px;color:var(--grey-text);text-align:justify;margin-top:3px}

.media-title{left:142px;top:777px;font-weight:700;color:#333}
.media-title .small{font-size:23px;line-height:22px;display:block}
.media-title .large{font-size:38px;line-height:38px;display:block}
.read-more{left:142px;top:860px;width:88px;height:26px;background:var(--red);color:#fff;font-size:13px;line-height:26px;text-align:center}
.media-divider{left:293px;top:769px;width:1px;height:122px;background:#ccc}
.media-article{left:321px;top:773px;width:738px}
.media-article h4{font-weight:400;font-size:15px;color:#222}
.media-article .dateline{font-size:13px;color:#999;margin-top:3px}
.media-article p{font-size:11.5px;line-height:17px;color:var(--grey-text);text-align:justify;margin-top:13px;letter-spacing:.2px}

.section-rule{left:155px;top:935px;width:890px;height:3px;background:radial-gradient(ellipse at center,#ccc 0%,rgba(255,255,255,0) 70%)}

.clients-title{left:141px;top:963px;font-family:"Roboto Condensed",Arial,sans-serif;font-weight:400;font-size:17.5px;color:var(--red)}
.client-row{left:150px;top:1005px;width:900px;height:36px;display:flex;justify-content:space-between;align-items:center}
.client{font-family:"Arimo",Arial,sans-serif;font-weight:700;font-size:18px;color:var(--logo-grey);display:flex;align-items:center;gap:6px}
.client i{display:inline-block;width:14px;height:14px;background:var(--logo-grey);border-radius:50%}

.footer-rule{left:141px;top:1074px;width:918px;height:1px;background:#e2e2e2}
.copyright{left:141px;top:1090px;font-size:11.5px;color:#444}
.footer-links{right:141px;top:1090px;font-size:11.5px;color:#444}
</style>
</head>
<body>

<header>
  <div class="abs brand">
    <div class="brand-name">TBW</div>
  </div>
  <div class="abs utility-links">Media Room<span>|</span>Contact Us</div>
  <div class="abs search">
    <div class="search-button">
      <svg width="31" height="26" viewBox="0 0 31 26" aria-hidden="true">
        <circle cx="14" cy="11" r="5" fill="none" stroke="#fff" stroke-width="2.2"/>
        <line x1="17.5" y1="14.5" x2="22" y2="19" stroke="#fff" stroke-width="3" stroke-linecap="round"/>
      </svg>
    </div>
  </div>
  <nav class="abs main-nav">
    <a class="active">Home</a>
    <a>Who We Are</a>
    <a>Transformational Consulting</a>
    <a>Who We Service</a>
    <a>Clientele</a>
    <a>Case Studies</a>
    <a>Insights</a>
  </nav>
</header>

<section class="abs hero">
  <div class="hero-photo" role="img" aria-label="Business people in suits assembling and climbing giant white jigsaw puzzle pieces"></div>
  <h1 class="hero-headline"><span class="sm">WE HELP IN </span><span class="lg">TRANSFORMING</span><br><span class="sm">YOUR </span><span class="lg">BUSINESS…</span></h1>
  <p class="hero-copy">Lorem ipsum dolor sit amet, consectetur adipiscing elit. In at metus eu ante pretium placerat eu id lectus. Aenean bibendum, arcu sed pharetra blandit, velit urna viverra mi, ac suscipit metus lacus ac metus.</p>
</section>

<section class="abs feature" style="left:141px">
  <h2>WHAT MAKES US DIFFERENT</h2>
  <h3>Integrating Finance, Business &amp;<br>Technology</h3>
  <p>TBW is truly unique and stands out by its end-to-end consulting expertise across all three Finance, Strategy and Technology. This gives TBW a huge advantage especially in cases where a comprehensive roadmap needs to be put in place encompassing all three elements. Companies employing this consulting model experience exponential results.</p>
</section>
<section class="abs feature" style="left:459px">
  <h2>OUR ALLIANCES</h2>
  <h3>Alliance with Hollister Crane, US</h3>
  <p>Our services and business solutions are strengthened by our alliance with Hollister Crane, a leading international consulting firm headquartered in the US. Hollister Crane delivers professional services in the areas of risk advisory, tax, and finance and accounting.</p>
</section>
<section class="abs feature" style="left:778px">
  <h2>INDUSTRY PRACTICE</h2>
  <h3>Banking &amp; Financial Services</h3>
  <p>In an effort to stay profitable, institutions have been taking various initiatives like across- the-board cost reductions, restructuring business through divestment of non-core/ non performing operations and staff retrenchment.</p>
</section>

<section class="media-room">
  <h2 class="abs media-title"><span class="small">THE MEDIA</span><span class="large">ROOM</span></h2>
  <div class="abs read-more">Read More</div>
  <div class="abs media-divider"></div>
  <article class="abs media-article">
    <h4>Hollister Crane announces expansion into the middle east</h4>
    <div class="dateline">MILWAUKEE – December 16, 2009</div>
    <p>Hollister Crane, a global provider of risk advisory, tax, and finance and accounting-related services, today announced it has established an alliance with Tall Birchwood Consulting, a leading business and technology consulting company in the United Arab Emirates. The alliance agreement, completed on September 28, 2009, marks Hollister Crane' third alliance this year and is its first expansion into the Middle East.</p>
  </article>
</section>

<div class="abs section-rule"></div>

<section class="clients">
  <h2 class="abs clients-title">OUR CLIENTS</h2>
  <div class="abs client-row">
    <span class="client"><i></i>Wirefold</span>
    <span class="client">Pagecrafter</span>
    <span class="client">Vitacore S.A.</span>
    <span class="client">Brightwire</span>
    <span class="client">Echoform</span>
    <span class="client">Northgate</span>
  </div>
</section>

<footer>
  <div class="abs footer-rule"></div>
  <div class="abs copyright">Copyright © 2011 TBW, All Rights Reserved</div>
  <div class="abs footer-links">Site Map | Legal Disclaimer</div>
</footer>

</body>
</html>
```